Kellwood Build, Carpentry Services

Business card for carpentry business in the Sunshine Coast.

Business card layout required using logo provided - provided both PDF copy and AI. Please let me know if you would like a the files for the logo symbol and text by itself.

Business Colours are grey, blue and white. The font colours codes for this design are Blue Hex # 00B4E6 and Hex # 39393B for the gray colour.

FYI font for logo is Gotham Bold.

Preference for a clean and striking layout that is simple and elegant.

Target Market(s)

Young Families, retirees, young couples requiring assistance with small to medium works/renovations on the Sunshine Coast.

Industry/Entity Type

Construction

Contact Information for Business Card

Dean Kellwood
Carpenter
0489305627
dean@kellwoodbuild.com.au
Palmview Bay, Coral Coast
RHPA Licensed Carpenter (In smaller font)

Font styles to use
Sans Serif

Colors

Designer to choose colors to be used in the design.

Requirements
Must have
• Logo provided must appear on the card, preferably on one side of the card by itself with the text on the alternate side
Nice to have
• Text on the other side of card, maybe grey background and white font here but happy for the designer to provide ideas here.
Should not have
• Use of other colours, other than the ones provided - white, grey and blue. Black optional.

```html
<!DOCTYPE html>
<html lang="en">
<head>
<meta charset="utf-8">
<title>Kellwood Build — Business Card</title>
<link href="https://fonts.googleapis.com/css2?family=Montserrat:wght@700&family=Roboto:wght@400;500&display=swap" rel="stylesheet">
<style>
  :root {
    --brand-blue: #00B4E6;
    --brand-grey: #39393B;
    --card-face: #D9D9D9;
    --card-line: #D9D9D9;
    --backdrop: #2B2B2D;
  }
  * { box-sizing: border-box; margin: 0; padding: 0; }
  html, body {
    width: 1200px; height: 900px; overflow: hidden;
    background: var(--backdrop);
  }
  .sheet {
    width: 1200px; height: 900px;
    display: flex; flex-direction: column; align-items: center; justify-content: center;
    gap: 30px;
  }
  .card {
    width: 640px; height: 366px;
    background: var(--card-face);
    border-radius: 26px;
    position: relative;
    overflow: hidden;
  }
  .wordmark {
    display: flex; align-items: center; gap: 14px;
    font-family: "Montserrat", sans-serif; font-weight: 700;
    color: var(--brand-blue);
    text-transform: uppercase;
    white-space: nowrap;
  }
  .wordmark__square { background: var(--brand-blue); flex: none; }
  .card--front { display: flex; align-items: center; justify-content: center; }
  .card--front .wordmark { font-size: 40px; }
  .card--front .wordmark__square { width: 40px; height: 40px; }

  .card--back .wordmark {
    position: absolute; left: 44px; top: 196px; font-size: 21px; gap: 9px;
  }
  .card--back .wordmark__square { width: 22px; height: 22px; }

  .contact {
    position: absolute; left: 330px; top: 62px;
    font-family: "Roboto", sans-serif; color: var(--brand-grey);
  }
  .contact__name {
    font-family: "Montserrat", sans-serif; font-weight: 700;
    color: var(--brand-blue); font-size: 27px; line-height: 1.1;
  }
  .contact__role { font-size: 19px; margin-top: 4px; margin-left: 14px; }
  .contact__licence { font-size: 10.5px; margin-left: 14px; margin-top: 2px; }
  .contact__list { list-style: none; margin-top: 22px; margin-left: 28px; }
  .contact__item {
    display: flex; align-items: center; gap: 10px;
    font-size: 16px; line-height: 1; height: 25px;
    white-space: nowrap;
  }
  .contact__icon { width: 15px; height: 15px; flex: none; }
</style>
</head>
<body>
<main class="sheet">
  <section class="card card--front" aria-label="Card front">
    <div class="wordmark"><span class="wordmark__square"></span>Kellwood Build</div>
  </section>

  <section class="card card--back" aria-label="Card back">
    <div class="wordmark"><span class="wordmark__square"></span>Kellwood Build</div>
    <div class="contact">
      <p class="contact__name">Dean Kellwood</p>
      <p class="contact__role">Carpenter</p>
      <p class="contact__licence">RHPA Licensed Carpenter</p>
      <ul class="contact__list">
        <li class="contact__item">
          <svg class="contact__icon" viewBox="0 0 24 24" aria-hidden="true"><path fill="#00B4E6" d="M6.6 10.8a15 15 0 0 0 6.6 6.6l2.2-2.2a1 1 0 0 1 1-.25 11.4 11.4 0 0 0 3.6.57 1 1 0 0 1 1 1V20a1 1 0 0 1-1 1A17 17 0 0 1 3 4a1 1 0 0 1 1-1h3.5a1 1 0 0 1 1 1c0 1.25.2 2.45.57 3.57a1 1 0 0 1-.25 1z"/></svg>
          0489305627
        </li>
        <li class="contact__item">
          <svg class="contact__icon" viewBox="0 0 24 24" aria-hidden="true"><rect x="2" y="5" width="20" height="14" rx="1" fill="#00B4E6"/><path d="M3 6l9 7 9-7" fill="none" stroke="#D9D9D9" stroke-width="1.6"/></svg>
          dean@kellwoodbuild.com.au
        </li>
        <li class="contact__item">
          <svg class="contact__icon" viewBox="0 0 24 24" aria-hidden="true"><circle cx="12" cy="12" r="10" fill="#00B4E6"/><path d="M2 12h20M12 2c3 3 3 17 0 20M12 2c-3 3-3 17 0 20" fill="none" stroke="#D9D9D9" stroke-width="1.3"/></svg>
          www.kellwoodbuild.com.au
        </li>
        <li class="contact__item">
          <svg class="contact__icon" viewBox="0 0 24 24" aria-hidden="true"><path fill="#00B4E6" d="M12 2a6 6 0 0 0-6 6c0 4.5 6 11 6 11s6-6.5 6-11a6 6 0 0 0-6-6zm0 8.5A2.5 2.5 0 1 1 12 5.5a2.5 2.5 0 0 1 0 5z"/><ellipse cx="12" cy="21" rx="6" ry="1.5" fill="none" stroke="#00B4E6" stroke-width="1.3"/></svg>
          Palmview Bay, Coral Coast
        </li>
      </ul>
    </div>
  </section>
</main>
</body>
</html>
```